Book Cover design: Waltz with a Heron.

I need a front and back cover for my book called 'Waltz with a Heron'.
It is self development book for help a person to be a better coach.
It is a metaphor. Dance is asking questions and the octopus is the person you are coaching (complex with my 'tentacles').
The audience would be adults. so want the cover to capture attention and also show that is have something of interest inside.
I have attach my first attempt. Please be bold.
The best sellers in this market place have simple but clear front page & back pages.

All the words are important but the sub-title is likely to change.

Target Market(s)

Adults who work with each other.
More business type people.

Industry/Entity Type

Leadership

Font styles to use
Serif

Requirements
Must have
• My project must have... The words that in the draft mock up.
• 'Waltz with a Heron' [TITLE]
• 'A Path to True Mentoring'[SUB-TITLE]
• How to create inspiration and accountability using
• Seven Pivotal Turns.[SUB_TITLE]
• By Rowan P Thistlewood
Nice to have
• Clever and simple.

```html
<!DOCTYPE html>
<html lang="en">
<head>
<meta charset="utf-8">
<title>Waltz with a Heron — Cover Spread</title>
<link rel="stylesheet" href="https://fonts.googleapis.com/css2?family=Marcellus&family=Arvo&display=swap">
<style>
  :root {
    --jade: #34b28a;
    --paper: #ffffff;
    --mist: rgba(190, 235, 218, 0.35);
  }
  * { margin: 0; padding: 0; box-sizing: border-box; }
  html, body { width: 1200px; height: 733px; overflow: hidden; background: var(--paper); }
  .cover {
    position: relative;
    width: 1200px;
    height: 733px;
    background: var(--paper);
    color: var(--jade);
    font-family: "Marcellus", serif;
    overflow: hidden;
  }
  .band { position: absolute; left: 0; width: 1200px; height: 13px; background: var(--jade); }
  .band--top { top: 20px; }
  .band--bottom { top: 700px; }
  .panel { position: absolute; top: 0; height: 733px; background: var(--jade); }
  .panel--back { left: 400px; width: 167px; }
  .panel--front { left: 633px; width: 167px; }

  .illustration {
    position: absolute;
    left: 334px;
    top: 134px;
    width: 550px;
    height: 540px;
    background: radial-gradient(ellipse at center, var(--mist) 0%, rgba(190,235,218,0.18) 60%, rgba(190,235,218,0) 100%);
    border-radius: 40%;
  }

  .spine {
    position: absolute;
    left: 567px;
    top: 33px;
    width: 66px;
    height: 667px;
    background: var(--paper);
    display: flex;
    flex-direction: column;
    align-items: center;
    padding-top: 18px;
  }
  .spine__author, .spine__title {
    writing-mode: vertical-rl;
    color: var(--jade);
    letter-spacing: 0.06em;
  }
  .spine__author { font-size: 19px; line-height: 24px; }
  .spine__title { font-size: 27px; margin-top: 40px; letter-spacing: 0.08em; }

  .back { position: absolute; left: 44px; top: 0; width: 290px; }
  .back__author { position: absolute; top: 104px; font-size: 19px; letter-spacing: 0.12em; white-space: nowrap; }
  .back__title { position: absolute; top: 163px; font-size: 23px; letter-spacing: 0.04em; white-space: nowrap; font-weight: 400; }
  .back__blurb, .back__note {
    position: absolute;
    width: 285px;
    font-family: "Arvo", serif;
    font-size: 10px;
    line-height: 13.4px;
    text-align: justify;
  }
  .back__blurb { top: 252px; }
  .back__note { top: 582px; text-align: left; }

  .front { position: absolute; right: 56px; top: 0; width: 330px; text-align: right; }
  .front__series { position: absolute; right: 0; top: 100px; font-size: 17px; letter-spacing: 0.08em; white-space: nowrap; }
  .front__title { position: absolute; right: 0; top: 163px; font-weight: 400; line-height: 1; white-space: nowrap; }
  .front__title-big { display: block; font-size: 54px; letter-spacing: 0.14em; margin-right: -0.14em; }
  .front__title-small { display: block; font-size: 24px; letter-spacing: 0.1em; margin: 2px -0.1em 4px 0; }
  .front__tagline { position: absolute; right: 0; top: 443px; font-size: 11px; line-height: 14px; letter-spacing: 0.1em; white-space: nowrap; }
  .front__author { position: absolute; right: 0; top: 607px; font-size: 20px; letter-spacing: 0.14em; margin-right: -0.14em; white-space: nowrap; }
</style>
</head>
<body>
<main class="cover">
  <div class="panel panel--back"></div>
  <div class="panel panel--front"></div>
  <div class="band band--top"></div>
  <div class="band band--bottom"></div>

  <div class="illustration" role="img" aria-label="White line drawing of a heron-like dancer with long curling limbs spreading across the back, spine and front cover"></div>

  <section class="back">
    <p class="back__author">ROWAN P THISTLEWOOD</p>
    <h2 class="back__title">WALTZ WITH A HERON</h2>
    <p class="back__blurb">Insert text Insert text Insert text Insert text Insert text Insert text Insert text Insert text Insert text Insert text Insert text Insert text Insert text Insert text Insert text Insert text Insert text Insert text Insert text Insert text Insert text Insert text Insert text Insert text Insert text Insert text Insert text Insert text Insert text Insert text Insert text Insert text Insert text Insert text Insert text Insert text Insert text Insert text Insert text Insert text Insert text Insert text Insert text Insert text Insert text Insert text Insert text Insert text Insert text Insert text Insert text Insert text Insert text Insert text Insert text Insert text Insert text Insert text Insert text Insert text Insert text Insert text Insert text Insert text Insert text Insert text Insert text Insert text Insert text Insert text Insert text Insert text Insert text Insert text Insert text Insert text Insert text Insert text Insert text Insert text Insert text Insert text Insert text Insert text Insert text Insert text Insert text</p>
    <p class="back__note">Insert text Insert text Insert text Insert text Insert text Insert text Insert text Insert text Insert text Insert text Insert text Insert text Insert text Insert text Insert text Insert text</p>
  </section>

  <aside class="spine">
    <p class="spine__author">ROWAN P<br>THISTLEWOOD</p>
    <p class="spine__title">WALTZ WITH A HERON</p>
  </aside>

  <section class="front">
    <p class="front__series">A PATH TO TRUE MENTORING</p>
    <h1 class="front__title">
      <span class="front__title-big">WALTZ</span>
      <span class="front__title-small">WITH A</span>
      <span class="front__title-big">HERON</span>
    </h1>
    <p class="front__tagline">HOW TO CREATE<br>INSPIRATION AND ACCOUNTABILITY USING<br>SEVEN PIVOTAL TURNS</p>
    <p class="front__author">ROWAN P THISTLEWOOD</p>
  </section>
</main>
</body>
</html>
```